Square graphic for social media post

I want to create a 1080 x 1080px all-black image for the quote below that I can share on social media. I want the emphasis to be primarily on the quote, secondarily on the portrait, and third (smallest) on the logo. I want the background on the portrait to be edited so it's transparent and just shows the face of the person on a black background (no brick wall visible).

Graphic color: black
Text color: white
Content: "What we went through is going to make the greatest generation of hoteliers our industry has ever seen." << biggest text
Dorian Welk << smaller text
President, Marrowgate Hotels << smaller text
[image of person - use whichever version looks better to you]
[Add Lodging Ledger logo - whichever looks better to you]

This image needs to be readable when sized down much smaller (400x400?) so want the text and portrait to take up most of the space.

I'd like the output both as PNG and original file (preferably Canva). Thanks!

Target Market(s)

Hotel managers

Industry/Entity Type

Hospitality

Font styles to use
Sans Serif

Colors

Designer to choose colors to be used in the design.

Requirements
Must have
• Needs to focus on the quote and the person quoted (the portrait)

```html
<!DOCTYPE html>
<html lang="en">
<head>
<meta charset="utf-8">
<title>Lodging Ledger — Quote Card</title>
<link href="https://fonts.googleapis.com/css2?family=Archivo+Narrow:ital,wght@0,400;0,600;1,400;1,600;1,700&display=swap" rel="stylesheet">
<style>
  :root {
    --ink: #000000;
    --paper: #ffffff;
    --pattern-tone: #1b1b1b;
    --top-band: #08090b;
    --portrait-light: #f4f4f6;
    --portrait-suit: #2b4c9a;
  }
  * { box-sizing: border-box; margin: 0; padding: 0; }
  html, body {
    width: 1200px;
    height: 1200px;
    overflow: hidden;
    background: var(--ink);
  }
  .quote-card {
    position: relative;
    width: 1200px;
    height: 1200px;
    background: var(--ink);
    color: var(--paper);
    font-family: "Archivo Narrow", "Arial Narrow", sans-serif;
    overflow: hidden;
  }
  .top-band {
    position: absolute;
    left: 0;
    top: 0;
    width: 1004px;
    height: 23px;
    background: var(--top-band);
  }
  .leaf-pattern {
    position: absolute;
    left: 0;
    top: 0;
    width: 465px;
    height: 1200px;
    background: linear-gradient(90deg, var(--pattern-tone) 0%, var(--pattern-tone) 70%, rgba(27,27,27,0) 100%);
  }
  .masthead {
    position: absolute;
    left: 378px;
    top: 218px;
    width: 400px;
    text-align: center;
    font-weight: 600;
    font-size: 34px;
    letter-spacing: 0.22em;
    text-transform: uppercase;
    color: var(--paper);
  }
  .quote {
    position: absolute;
    left: 44px;
    top: 524px;
    font-style: italic;
    font-weight: 700;
  }
  .quote__lead,
  .quote__tail {
    font-size: 33px;
    line-height: 37px;
  }
  .quote__emphasis {
    font-size: 40px;
    line-height: 54px;
    text-transform: uppercase;
    margin: 8px 0 2px;
  }
  .attribution {
    position: absolute;
    left: 43px;
    top: 866px;
    font-style: italic;
  }
  .attribution__name {
    font-weight: 700;
    font-size: 38px;
    line-height: 46px;
  }
  .attribution__role {
    margin-top: 50px;
    font-weight: 400;
    font-size: 33px;
    line-height: 45px;
    letter-spacing: 0.02em;
  }
  .portrait-frame {
    position: absolute;
    left: 0;
    top: 0;
    width: 1200px;
    height: 1200px;
    pointer-events: none;
  }
</style>
</head>
<body>
  <main class="quote-card">
    <div class="top-band"></div>
    <div class="leaf-pattern" role="img" aria-label="Faint dark leaf pattern decoration"></div>

    <div class="masthead">Lodging Ledger</div>

    <blockquote class="quote">
      <p class="quote__lead">What we went through<br>is going to make</p>
      <p class="quote__emphasis">The greatest generation<br>of hoteliers</p>
      <p class="quote__tail">our industry has<br>ever seen.</p>
    </blockquote>

    <div class="attribution">
      <p class="attribution__name">Dorian Welk</p>
      <p class="attribution__role">President,<br>Marrowgate Hotels</p>
    </div>

    <svg class="portrait-frame" viewBox="0 0 1200 1200" xmlns="http://www.w3.org/2000/svg">
      <defs>
        <linearGradient id="portrait-tones" x1="0" y1="0" x2="0" y2="1">
          <stop offset="0" stop-color="var(--portrait-light)"/>
          <stop offset="0.55" stop-color="#e7c2ab"/>
          <stop offset="0.8" stop-color="var(--portrait-suit)"/>
          <stop offset="1" stop-color="var(--portrait-suit)"/>
        </linearGradient>
      </defs>
      <circle class="portrait-ring" cx="1150" cy="935" r="590" fill="none" stroke="#ffffff" stroke-width="2.5"/>
      <circle class="portrait" cx="1150" cy="935" r="545" fill="url(#portrait-tones)" role="img" aria-label="Portrait photo of Dorian Welk in a blue blazer and white shirt"/>
    </svg>
  </main>
</body>
</html>
```